Pinwheel Coffee Co. Fundraising Brochure

Our coffee company (www.pinwheelcoffee.example) is wanting to launch a fundraising option for people / schools to use. I have designed a MOCK UP but I need a real design, with the real info and good images, good layout, etc. I want to print it as an 11 x 17 and fold it twice. You can find images and the look of our material at www.pinwheelcoffee.example

Target Market(s)

School PTF
Trail Ranger troops
Moms

Industry/Entity Type

It Company

Font styles to use
Serif

Colors

Designer to choose colors to be used in the design.

Requirements
Must have
• Must mirror the look and feel of our website www.PinwheelCoffee.example

```html
<!DOCTYPE html>
<html lang="en">
<head>
<meta charset="utf-8">
<title>Pinwheel Coffee Co. Fundraising Brochure</title>
<link href="https://fonts.googleapis.com/css2?family=Alfa+Slab+One&family=Arimo:wght@400;700&family=Oswald:wght@600&display=swap" rel="stylesheet">
<style>
:root{
  --cream:#f2e3bd;
  --cream-deep:#e6cf98;
  --gold:#dfa126;
  --brown:#3a2314;
  --ink:#24170e;
  --paper:#fbf9f4;
  --red:#b6421f;
  --green:#2f7a3e;
  --blue:#2d5f9b;
  --label-cream:#efe2c6;
  --stage:#e9e4dc;
}
*{box-sizing:border-box;margin:0;padding:0}
html,body{width:1200px;height:849px;overflow:hidden;background:var(--stage)}
body{font-family:"Arimo",Arial,sans-serif;color:var(--ink)}
.spread{position:absolute;inset:0;display:flex}
.page{position:relative;width:600px;height:849px;background:var(--paper);overflow:hidden}
.page--left{border-right:1px solid #d8d2c6}
.masthead{position:absolute;left:0;top:0;width:100%;height:190px;background:linear-gradient(180deg,var(--cream) 0%,var(--cream-deep) 100%)}
.band-dark{position:absolute;height:26px;background:var(--brown)}
.band-gold{position:absolute;height:26px;background:var(--gold)}
.beans{position:absolute;border-radius:40%;background:radial-gradient(circle at 40% 40%,#7a4526,#3a1d0e)}
.slab{font-family:"Alfa Slab One",Georgia,serif;color:var(--brown);text-transform:uppercase;letter-spacing:1px}
.intro-title{position:absolute;left:150px;top:118px;line-height:1}
.intro-title .big{font-size:36px;display:block}
.intro-title .small{font-size:21px;display:block;margin-top:2px}
.tab{position:absolute;background:var(--gold);padding:6px 22px;font-family:"Alfa Slab One",Georgia,serif;color:var(--brown);font-size:22px;line-height:1.2;text-transform:uppercase;letter-spacing:1px}
.steps{position:absolute;left:90px;top:276px;font-size:13.5px;line-height:1.3;list-style:none}
.press{position:absolute;left:0;top:330px;width:170px;height:320px;border-radius:0 30px 20px 0;background:linear-gradient(90deg,#b9b9b9,#eeeeee 40%,#8c6a4b 60%,#5b3a22)}
.row-label{position:absolute;font-size:12px;font-weight:700;text-align:center;width:420px;left:170px}
.bag{position:absolute;width:84px;height:76px;border-radius:3px;display:flex;flex-direction:column;align-items:center;justify-content:center;color:#fff;box-shadow:0 2px 4px rgba(0,0,0,.25)}
.bag .name{font-family:"Oswald",sans-serif;font-size:15px;letter-spacing:.5px;text-transform:uppercase}
.bag .maker{font-size:6px;margin-top:8px;letter-spacing:.5px;text-transform:uppercase;text-align:center}
.bag--hearthside{background:var(--red)}
.bag--frontier{background:var(--green)}
.bag--summit{background:var(--blue)}
.bag--union{background:var(--label-cream);color:var(--red);border:3px solid #d9c79f}
.bag--union .name{color:var(--blue)}
.price{position:absolute;z-index:2;width:36px;height:36px;border-radius:50%;background:var(--gold);border:2px solid var(--brown);font-family:"Alfa Slab One",Georgia,serif;font-size:11px;display:flex;align-items:center;justify-content:center;color:var(--brown)}
.rule{position:absolute;left:170px;width:420px;height:1px;background:#bbb}
.foot{position:absolute;left:0;bottom:0;width:100%;background:linear-gradient(180deg,var(--cream-deep),var(--cream))}
.foot--left{height:160px}
.news-title{position:absolute;top:12px;width:100%;text-align:center;font-weight:700;font-size:15px}
.news-copy{position:absolute;top:36px;left:110px;width:380px;text-align:center;font-weight:700;font-size:11px;line-height:1.3;text-transform:uppercase}
.brand{position:absolute;right:34px;top:92px;display:flex;align-items:center;gap:8px;font-family:"Alfa Slab One",Georgia,serif;font-size:15px;color:var(--brown)}
.brand .dot{width:22px;height:22px;border-radius:50%;background:var(--gold)}
.site{position:absolute;left:28px;bottom:16px;font-weight:700;font-size:16px}
.tagline{position:absolute;right:60px;top:70px;text-align:center;font-family:"Alfa Slab One",Georgia,serif;color:var(--brown);font-size:19px;line-height:1.2}
.lead{position:absolute;left:30px;top:262px;width:540px;font-size:11.5px;line-height:1.35}
.roast{position:absolute;width:265px;height:96px}
.roast .photo{position:absolute;left:0;top:0;width:88px;height:88px;border-radius:50%;border:4px solid var(--gold);background:radial-gradient(circle at 45% 40%,#8a5a34,#3a1d0e)}
.roast h3{position:absolute;left:98px;top:2px;font-size:11px}
.roast p{position:absolute;left:98px;top:18px;width:165px;font-size:8.5px;line-height:1.3}
.roast-names{position:absolute;left:30px;top:548px;font-weight:700;font-size:14px;word-spacing:16px}
.roast-copy{position:absolute;left:30px;top:570px;width:545px;font-size:10.5px;line-height:1.35}
.roast-copy p+p{margin-top:6px}
.foot--right{height:120px}
.offer{position:absolute;left:40px;top:22px;width:520px;text-align:center;font-weight:700;font-size:14px;line-height:1.45}
</style>
</head>
<body>
<div class="spread">

  <section class="page page--left">
    <header class="masthead">
      <div class="beans" role="img" aria-label="Roasted coffee beans" style="left:30px;top:118px;width:100px;height:58px"></div>
      <h1 class="slab intro-title"><span class="big">Introducing</span><span class="small">Pinwheel Coffee Co.</span></h1>
    </header>
    <div class="band-dark" style="left:0;top:190px;width:380px"></div>
    <div class="band-gold" style="left:380px;top:196px;width:220px;height:20px"></div>
    <div class="band-dark" style="left:0;top:226px;width:600px;height:14px"></div>
    <h2 class="tab" style="left:20px;top:234px">Coffee Plans</h2>

    <ol class="steps">
      <li>1. Collect Orders with the Credit Card authorization FORMS included.</li>
      <li>2. Submit to sales@PinwheelCoffee.example or call 555.010.4821!</li>
      <li>3. Done! It's that easy! We do all the rest and cut you a check!</li>
    </ol>

    <div class="press" role="img" aria-label="French press filled with coffee"></div>

    <p class="row-label" style="top:325px">Individual Bags Sold:</p>
    <div class="price" style="left:158px;top:322px">$25</div>
    <div class="bag bag--hearthside" style="left:180px;top:342px"><span class="name">Hearthside</span><span class="maker">Pinwheel Coffee Co.</span></div>
    <div class="bag bag--frontier" style="left:280px;top:342px"><span class="name">Frontier</span><span class="maker">Pinwheel Coffee Co.</span></div>
    <div class="bag bag--summit" style="left:380px;top:342px"><span class="name">Summit</span><span class="maker">Pinwheel Coffee Co.</span></div>
    <div class="bag bag--union" style="left:480px;top:342px"><span class="name">Union</span><span class="maker">Pinwheel Coffee Co.</span></div>
    <div class="rule" style="top:428px"></div>

    <p class="row-label" style="top:436px">Best Value!! 2-Week Subscriptions (1 Bag Every 2 Weeks) Sold:</p>
    <div class="price" style="left:556px;top:434px">$22</div>
    <div class="bag bag--hearthside" style="left:180px;top:456px"><span class="name">Hearthside</span><span class="maker">Pinwheel Coffee Co.</span></div>
    <div class="bag bag--frontier" style="left:280px;top:456px"><span class="name">Frontier</span><span class="maker">Pinwheel Coffee Co.</span></div>
    <div class="bag bag--summit" style="left:380px;top:456px"><span class="name">Summit</span><span class="maker">Pinwheel Coffee Co.</span></div>
    <div class="bag bag--union" style="left:480px;top:456px"><span class="name">Union</span><span class="maker">Pinwheel Coffee Co.</span></div>
    <div class="rule" style="top:542px"></div>

    <p class="row-label" style="top:550px">4-week Subscriptions (1 Bag Every 4 Weeks) Sold:</p>
    <div class="price" style="left:158px;top:568px">$23</div>
    <div class="bag bag--hearthside" style="left:180px;top:570px"><span class="name">Hearthside</span><span class="maker">Pinwheel Coffee Co.</span></div>
    <div class="bag bag--frontier" style="left:280px;top:570px"><span class="name">Frontier</span><span class="maker">Pinwheel Coffee Co.</span></div>
    <div class="bag bag--summit" style="left:380px;top:570px"><span class="name">Summit</span><span class="maker">Pinwheel Coffee Co.</span></div>
    <div class="bag bag--union" style="left:480px;top:570px"><span class="name">Union</span><span class="maker">Pinwheel Coffee Co.</span></div>

    <footer class="foot foot--left">
      <h3 class="news-title">KEEP YOUR INBOX FRESH</h3>
      <p class="news-copy">Get brewprints delivered fresh to your inbox. Brewing and food pairing tips, recipes and offers. Sign up now at www.pinwheelcoffee.example/news</p>
      <div class="brand"><span class="dot"></span>Pinwheel Coffee Co.</div>
      <p class="site">www.PinwheelCoffee.example</p>
    </footer>
  </section>

  <section class="page page--right">
    <header class="masthead">
      <div class="beans" role="img" aria-label="Roasted coffee beans" style="left:30px;top:120px;width:80px;height:50px"></div>
      <p class="tagline">We Don't roast 'til you order,<br>SO HURRY UP!</p>
    </header>
    <div class="band-dark" style="left:0;top:190px;width:380px"></div>
    <div class="band-gold" style="left:380px;top:196px;width:220px;height:20px"></div>
    <h2 class="tab" style="left:20px;top:214px">Our Coffee</h2>

    <p class="lead">We're small-batch roasters of high quality, responsibly sourced coffee. We don't roast until you order, so you can be assured the beans you brew are as fresh as you can get without roasting them yourself.</p>

    <article class="roast" style="left:30px;top:302px">
      <div class="photo" role="img" aria-label="Hearthside Roast bag on coffee beans"></div>
      <h3>Hearthside Roast</h3>
      <p>Pairs well with pastries and lighter desserts. With forward acids, it's adventurous yet not overpowering, with a smooth clean finish.</p>
    </article>
    <article class="roast" style="left:305px;top:298px">
      <div class="photo" role="img" aria-label="Summit Roast bag on coffee beans"></div>
      <h3>Summit Roast</h3>
      <p>Aggressive and dynamic, our dark Summit Roast cannot be ignored. Rich flavor pairs with afternoon snacks and late-night talks, with notes of dark chocolate and cherry.</p>
    </article>
    <article class="roast" style="left:30px;top:398px">
      <div class="photo" role="img" aria-label="Frontier Roast bag on coffee beans"></div>
      <h3>Frontier Roast</h3>
      <p>A balanced, yet lively, bold but never harsh medium dark roast from single origin beans. Its full body pairs well with savory and sweet treats.</p>
    </article>
    <article class="roast" style="left:305px;top:394px">
      <div class="photo" role="img" aria-label="Union Blend bag on coffee beans"></div>
      <h3>Union Blend</h3>
      <p>A revolutionary concoction of dark and medium-dark roasts to start your day off with a bang. Our motto for this blend? E Pluribus Beanum!</p>
    </article>

    <div class="band-dark" style="left:0;top:496px;width:600px;height:12px"></div>
    <h2 class="tab" style="left:20px;top:504px;font-size:17px">What Roast Do I Want?</h2>

    <p class="roast-names">Hearthside, Frontier, Summit, Union</p>
    <div class="roast-copy">
      <p>Pinwheel's Hearthside Roast pairs well with pastries and lighter desserts. With forward acids, it's adventurous yet not overpowering, with a smooth clean finish. Whether you're starting the day off on your front porch swing or entertaining your guests after dinner, our inviting and hospitable Hearthside Roast fits the bill.</p>
      <p>A subtle earthiness and hardy mouthfeel make Frontier roast a very satisfying single cup choice. If you can only have one cup of coffee a day, make it a cup of Frontier Roast. Its full body pairs well with savory and sweet treats.</p>
      <p>A revolutionary concoction of dark and medium-dark roasts to start your day off with a bang -- the same way our nation's founders started theirs! Our motto for this blend? E Pluribus Beanum -- out of many beans, one fantastic coffee!</p>
    </div>

    <footer class="foot foot--right">
      <p class="offer">Subscribe to a 2 OR 4 week plan &amp; receive a FREE French Press with your first order! All subscribers will be provided with an online account and can update quantity and roast or cancel at any time by logging into account.</p>
    </footer>
  </section>

</div>
</body>
</html>
```